Business Card Design Project

Looking for a simple and stylish business card. We are an Advertising Company. The card Must feature the company logo (attached) and also this info.
p: 0461528390
e: sales@jh-promo.com.au
w: www.jh-promo.com.au
We Advertise mainly using TV screens featured in restaurants and cafe. See website for more about the business.
Not really looking for a plain background, but at the same time do not want to much happening in the Background. I am not really to fussy though with the design or the colour scheme, and I am leaving the creativity part up to you creative designers.
Business

```html
<!DOCTYPE html>
<html lang="en">
<head>
<meta charset="utf-8">
<title>JH Promo Business Card</title>
<link rel="stylesheet" href="https://fonts.googleapis.com/css2?family=Questrial&display=swap">
<style>
  :root {
    --backdrop: #e9e9ec;
    --card: #ffffff;
    --pink: #e0186e;
    --pink-soft: #e58aae;
    --pink-faint: #f2c4d6;
    --blue: #1f4f9c;
    --blue-soft: #8ea6cc;
  }
  * { margin: 0; padding: 0; box-sizing: border-box; }
  html, body {
    width: 1200px; height: 900px; overflow: hidden;
    background: var(--backdrop);
    font-family: "Questrial", "Century Gothic", sans-serif;
  }
  .canvas { position: relative; width: 1200px; height: 900px; }
  .card {
    position: absolute; left: 250px;
    width: 700px; height: 400px;
    background: var(--card);
    overflow: hidden;
    box-shadow: 0 6px 22px rgba(0,0,0,0.18);
  }
  .card--back { top: 40px; }
  .card--front { top: 460px; }

  /* back side */
  .back-name {
    position: absolute; left: 22px; bottom: 90px;
    font-size: 126px; line-height: 1; letter-spacing: 2px;
    color: var(--blue); white-space: nowrap;
  }
  .back-web {
    position: absolute; right: 40px; bottom: 40px;
    font-size: 17px; color: var(--blue);
  }

  /* front side */
  .contact { position: absolute; left: 38px; top: 44px; }
  .contact__name { font-size: 27px; color: var(--pink); line-height: 1.1; }
  .contact__role { font-size: 20px; color: var(--blue); margin-bottom: 26px; }
  .contact__line {
    display: flex; align-items: center; gap: 10px;
    font-size: 20px; color: var(--blue); margin-bottom: 8px;
  }
  .contact__line svg { width: 16px; height: 16px; flex: none; }

  .echo {
    position: absolute; right: 16px; white-space: nowrap;
    line-height: 1; letter-spacing: 1px; text-align: right;
  }
  .echo--1 { top: 16px; font-size: 30px; color: var(--blue); }
  .echo--2 { top: 50px; font-size: 46px; color: var(--pink-soft); }
  .echo--3 { top: 102px; font-size: 70px; color: var(--blue-soft); }
  .echo--4 { top: 238px; font-size: 126px; color: var(--pink-faint); }
</style>
</head>
<body>
<div class="canvas">

  <section class="card card--back" aria-label="Card back">
    <div class="back-name">JH PROMO</div>
    <div class="back-web">www.jh-promo.com.au</div>
  </section>

  <section class="card card--front" aria-label="Card front">
    <div class="echo echo--4" aria-hidden="true">JH PROMO</div>
    <div class="echo echo--3" aria-hidden="true">JH PROMO</div>
    <div class="echo echo--2" aria-hidden="true">JH PROMO</div>
    <div class="echo echo--1">JH PROMO</div>

    <div class="contact">
      <div class="contact__name">Mark Delaney</div>
      <div class="contact__role">Account Manager</div>
      <div class="contact__line">
        <svg viewBox="0 0 16 16" aria-hidden="true">
          <rect x="1" y="3.5" width="14" height="9" fill="var(--pink)"/>
          <path d="M1 3.5 L8 9 L15 3.5" fill="none" stroke="#fff" stroke-width="1.2"/>
        </svg>
        <span>sales@jh-promo.com.au</span>
      </div>
      <div class="contact__line">
        <svg viewBox="0 0 16 16" aria-hidden="true">
          <circle cx="8" cy="8" r="7" fill="none" stroke="var(--pink)" stroke-width="1.4"/>
          <path d="M5.5 4.5 L7 4.5 L7.6 6.4 L6.7 7.2 Q7.6 8.9 9 9.6 L9.8 8.7 L11.5 9.3 L11.5 10.8 Q8.4 11.4 6.3 9 Q4.6 7 5.5 4.5 Z" fill="var(--pink)"/>
        </svg>
        <span>0461 528 390</span>
      </div>
    </div>
  </section>

</div>
</body>
</html>
```